New Fun, Positive, energised looking Business Card Needed for High Achiever Coach

I am looking for a two sided full colour business card. I am self employed and have recently re branded my 1-2-1 work re-vitalising high achievers. My target client base for these cards is therefore high achievers - usually aged 40 -55, they are often entrepreneurs, CEO or work in banking and finance and 2/3 are male. I work with them on 90 day or 6 month coaching programs to help them live their success in a healthier, more sustainable and fulfiiled way. They pay for this privately so though they are corporate types the cards need not look 'corporate'. I want to portray the idea of transformation, vitality and re-connecting.
You can get a feel for the look I like on my new website: norvemitch.co.uk
I want to use this logo with strapline (Re-Vitalising High Achievers) (I purchased off Glyphmart) and font/ colours (the turquoise and green).
Details to include on the card:
www.norvemitch.co.uk
+44 7915 302684
petra@norvemitch.co.uk
skype: norvemitch
I'd also like to include:
Do you struggle to switch off? Want to be healthier and feel fitter? Want closer relationships? More clarity over the direction you are headed? I can help you do these things using integrated mind-body techniques. Visit norvemitch.co.uk TODAY to apply for a FREE Breakthrough session.
BUT if that is too much text for a card I am open to advice/ammendments.
Updates
Thanks for your design - I am considering them. PLease change the wording to :

```html
<!DOCTYPE html>
<html lang="en">
<head>
<meta charset="utf-8">
<title>Petra Norvemitch – Business Card</title>
<link rel="stylesheet" href="https://fonts.googleapis.com/css2?family=Mulish:wght@700;800&display=swap">
<style>
  :root {
    --turquoise: #1b9dc0;
    --turquoise-dark: #1a7f9b;
    --green: #5fb66a;
    --card-light: #ffffff;
    --card-edge: #e1e1e3;
    --backdrop: #d4d4d4;
    --white: #ffffff;
  }
  * { margin: 0; padding: 0; box-sizing: border-box; }
  html, body {
    width: 1200px; height: 1181px; overflow: hidden;
    background: var(--backdrop);
    font-family: "Mulish", sans-serif;
  }
  .canvas { position: relative; width: 1200px; height: 1181px; }

  .card {
    position: absolute; left: 216px; width: 767px; height: 441px;
    background: radial-gradient(ellipse at 50% 50%, var(--card-light) 0%, #f3f3f4 40%, var(--card-edge) 100%);
    box-shadow: 0 6px 14px rgba(0,0,0,0.25);
    overflow: hidden;
  }
  .card--front { top: 96px; }
  .card--back { top: 635px; height: 440px; }

  .top-band { position: absolute; top: 0; left: 0; right: 0; height: 12px; background: var(--turquoise); }

  .bottom-bands { position: absolute; left: 0; right: 0; bottom: 0; height: 13px; display: flex; gap: 2px; background: var(--white); }
  .bottom-bands span { flex: 0 0 auto; }
  .seg-side { width: 251px; background: var(--turquoise); }
  .seg-mid { width: 261px; background: var(--green); }

  .brand {
    position: absolute; top: 170px; left: 0; right: 0;
    display: flex; align-items: center; justify-content: center; gap: 18px;
  }
  .brand-dot { width: 22px; height: 22px; border-radius: 50%; background: var(--green); }
  .brand-name { font-weight: 800; font-size: 40px; color: var(--turquoise); letter-spacing: 0.5px; }

  .pitch {
    position: absolute; top: 124px; left: 0; right: 0;
    text-align: center; font-weight: 700; font-size: 15.5px; line-height: 20px;
    color: var(--turquoise-dark);
  }
  .pitch .accent { color: var(--green); }

  .contact-strip { position: absolute; left: 0; right: 0; top: 315px; height: 12px; background: var(--turquoise); }
  .contact-row {
    position: absolute; left: 0; right: 0; bottom: 0; height: 111px;
    display: flex; gap: 2px; background: var(--white);
  }
  .contact-cell {
    display: flex; flex-direction: column; align-items: center; justify-content: center;
    color: var(--white); font-weight: 700; font-size: 13.5px; line-height: 16px; text-align: center;
  }
  .contact-cell--side { width: 251px; background: var(--turquoise); }
  .contact-cell--mid { width: 261px; background: var(--green); font-size: 18px; font-weight: 800; }
</style>
</head>
<body>
<main class="canvas">

  <section class="card card--front" aria-label="Card front">
    <div class="top-band"></div>
    <div class="brand">
      <span class="brand-dot"></span>
      <span class="brand-name">Petra Norvemitch</span>
    </div>
    <div class="bottom-bands">
      <span class="seg-side"></span><span class="seg-mid"></span><span class="seg-side"></span>
    </div>
  </section>

  <section class="card card--back" aria-label="Card back">
    <div class="top-band"></div>
    <p class="pitch">
      Do you struggle to switch off ? Want to be healthier and feel fitter ?<br>
      Want closer relationships ? More clarity over the direction you are headed ?<br>
      I can help you do these things using integrated mind-body techniques.<br>
      Visit <span class="accent">norvemitch.co.uk</span> TODAY to apply for a <span class="accent">FREE</span> Breakthrough session.
    </p>
    <div class="contact-strip"></div>
    <div class="contact-row">
      <div class="contact-cell contact-cell--side">
        <span>+44 7915 302684</span>
        <span>skype: norvemitch</span>
      </div>
      <div class="contact-cell contact-cell--mid">
        <span>Petra Norvemitch</span>
      </div>
      <div class="contact-cell contact-cell--side">
        <span>www.norvemitch.co.uk</span>
        <span>petra@norvemitch.co.uk</span>
      </div>
    </div>
  </section>

</main>
</body>
</html>
```